Business Card for Vorlo Parts Wholesale supplier

Hi There! I need a new business card for our company. We are specialized in selling Vorlo parts, mostly we sell new LCD screens for uDialr and oTabs. I would like to see that back in the design.

You can find the colors and logo's on our website: www.darvok.nl

Industry/Entity Type

Business

Contact Information for Business Card

My Details:
Bas Hollink

Phone: 0031627381946
E-mail: Bas@darvok.nl

Slogan: "Because Quality Matters"

Font styles to use
Sans Serif

Colors

Designer to choose colors to be used in the design.

Requirements
Must have
• A Black backside with the Darvok logo on it. The front side should be clean with only my contact details.
• But I'm also open for something really different or awesome!
Nice to have
• Remember that we are in the parts & repairing industry, So i'll be handing those business cards mainly to repair companies. Maybe you can do something with that thought :)

```html
<!DOCTYPE html>
<html lang="en">
<head>
<meta charset="utf-8">
<title>Darvok business card</title>
<link rel="stylesheet" href="https://fonts.googleapis.com/css2?family=Open+Sans:wght@400;600;700&family=Roboto:wght@300;400&display=swap">
<style>
  :root {
    --backdrop-top: #b3b3b3;
    --backdrop-bottom: #a6a6a6;
    --card-white: #ffffff;
    --card-dark: #4a4a47;
    --ink: #111111;
    --mark-grey: #a3a3a3;
    --photo-light: #6a6a67;
    --photo-dark: #2e2e2c;
    --on-dark: #ffffff;
    --on-dark-soft: #e6e2d4;
  }
  html, body {
    margin: 0;
    padding: 0;
    width: 1200px;
    height: 900px;
    overflow: hidden;
  }
  body {
    position: relative;
    background: linear-gradient(180deg, var(--backdrop-top), var(--backdrop-bottom));
    font-family: "Open Sans", Arial, sans-serif;
  }
  .card {
    position: absolute;
    top: 170px;
    width: 347px;
    height: 561px;
    box-shadow: 0 1px 3px rgba(0,0,0,0.15);
    overflow: hidden;
  }
  .card--front { left: 259px; background: var(--card-white); color: var(--ink); }
  .card--back { left: 631px; background: var(--card-dark); color: var(--on-dark); }

  .brand-dot {
    position: absolute;
    left: 130px;
    top: 87px;
    width: 88px;
    height: 88px;
    border-radius: 50%;
    background: var(--mark-grey);
  }
  .brand-name {
    position: absolute;
    left: 0;
    right: 0;
    top: 188px;
    text-align: center;
    font-size: 76px;
    font-weight: 600;
    letter-spacing: 1px;
    line-height: 1;
  }
  .holder-name {
    position: absolute;
    left: 0; right: 0;
    top: 345px;
    text-align: center;
    font-size: 22px;
    font-weight: 600;
    letter-spacing: 1px;
    margin: 0;
  }
  .contact-icons {
    position: absolute;
    left: 0; right: 0;
    top: 397px;
    display: flex;
    justify-content: center;
    gap: 4px;
  }
  .contact-list {
    position: absolute;
    left: 0; right: 0;
    top: 425px;
    margin: 0;
    padding: 0;
    list-style: none;
    text-align: center;
    font-size: 15px;
    line-height: 20px;
  }
  .slogan {
    position: absolute;
    left: 0; right: 0;
    top: 508px;
    margin: 0;
    text-align: center;
    font-size: 18px;
    font-weight: 700;
    letter-spacing: 0.3px;
  }

  .device-photo {
    position: absolute;
    left: 0;
    top: 160px;
    width: 347px;
    height: 240px;
    background:
      radial-gradient(ellipse 60% 45% at 85% 45%, rgba(20,20,20,0.6), transparent 70%),
      linear-gradient(180deg, var(--card-dark) 0%, var(--photo-light) 35%, var(--photo-dark) 70%, var(--card-dark) 100%);
  }
  .back-brand {
    position: absolute;
    left: 0; right: 0;
    top: 234px;
    display: flex;
    align-items: center;
    justify-content: center;
    gap: 10px;
  }
  .back-brand .rule {
    width: 52px;
    height: 1px;
    background: var(--on-dark);
  }
  .back-brand .brand-small {
    font-family: "Open Sans", Arial, sans-serif;
    font-size: 17px;
    font-weight: 600;
    color: var(--on-dark);
  }
  .claim {
    position: absolute;
    left: 0; right: 0;
    margin: 0;
    text-align: center;
    font-family: "Roboto", Arial, sans-serif;
  }
  .claim--lead { top: 275px; font-size: 19px; font-weight: 300; color: var(--on-dark-soft); }
  .claim--main { top: 306px; font-size: 23px; font-weight: 400; color: var(--on-dark); }
</style>
</head>
<body>
  <section class="card card--front" aria-label="Front of card">
    <div class="brand-dot"></div>
    <div class="brand-name">darvok</div>
    <h1 class="holder-name">BAS HOLLINK</h1>
    <div class="contact-icons" aria-hidden="true">
      <svg width="14" height="14" viewBox="0 0 14 14"><path d="M3 1.5 L5 1 L6.3 4 L5 5.2 C5.8 7 7 8.2 8.8 9 L10 7.7 L13 9 L12.5 11 C12 12.5 10 13 8 12 C5 10.5 3.5 9 2 6 C1 4 1.5 2 3 1.5Z" fill="#111"/></svg>
      <svg width="15" height="14" viewBox="0 0 15 14"><rect x="1" y="3" width="13" height="9" fill="#111"/><path d="M1 3.5 L7.5 8.5 L14 3.5" fill="none" stroke="#fff" stroke-width="1.2"/></svg>
      <svg width="14" height="14" viewBox="0 0 14 14"><circle cx="7" cy="7" r="6" fill="#111"/><path d="M4 4 C6 5 5 7 7 8 C8 9 7 11 6 12 M9 2.5 C8.5 4 10 5 12 5" fill="none" stroke="#fff" stroke-width="1.2"/></svg>
    </div>
    <ul class="contact-list">
      <li>0031627381946</li>
      <li>Bas@darvok.nl</li>
      <li>www.darvok.nl</li>
    </ul>
    <p class="slogan">BECAUSE QUALITY MATTERS</p>
  </section>

  <section class="card card--back" aria-label="Back of card">
    <div class="device-photo" role="img" aria-label="Close-up photo of a smartphone with a cracked screen"></div>
    <div class="back-brand">
      <span class="rule"></span>
      <span class="brand-small">darvok</span>
      <span class="rule"></span>
    </div>
    <p class="claim claim--lead">The highest quality</p>
    <p class="claim claim--main">OEM parts</p>
  </section>
</body>
</html>
```